Real Estate Company Looking for Business Card Designs for 3 Executives

Hello!
Thanks so much for considering our project! We are a real estate investment company located in Edmonton, Alberta called Marlbeck Group of Companies. We invest/develop both commercial and residential real estate and are looking to create 3 DOUBLE-SIDED business cards for 3 top executives in the company! (for some reason it won't let us select the double-sided option, but yes, the cards are double sided and would be happy to tip extra)

We have certain guidelines that we want our business cards to for sure follow - the back of the Business card has to be the Black Background Version of the Logo which has already been designed and linked as a file (first file). We want the entire back of the card to simply just be the black background logo. In terms of the front of the card, would like to see a smaller version of the white background logo (linked as the second file) in the top left hand corner - of course, feel free to get creative and we can make revisions together along the way! and Then after that, just text. We want the card to be sharp, clean, easy on the eyes and highly professional looking. We would like the card to include the Full name of the Company (Marlbeck Group of Companies), Name of the Person, Title, Phone, Email. If possible please provide the front part of the card for 3 people:

1) Marlbeck Group of Companies, Lena Okafor, Chief Financial Officer, 780-555-0162, lenaokafor@marlbeckgroup.example

2) Marlbeck Group of Companies, Tobias Okafor, Chief Executive Officer, 780-555-0148, tobiasokafor@marlbeckgroup.example

3) Marlbeck Group of Companies, Rui Dalton, Chief Operations Officer, 587-555-0193, ruidalton@marlbeckgroup.example

Thank you so much for considering our project & we look forward to seeing your designs!

```html
<!DOCTYPE html>
<html lang="en">
<head>
<meta charset="utf-8">
<title>Marlbeck Group of Companies — Business Card</title>
<link href="https://fonts.googleapis.com/css2?family=Arimo:wght@400&family=Tinos:wght@700&display=swap" rel="stylesheet">
<style>
  :root {
    --backdrop: #2b2b2b;
    --card: #1e1e1e;
    --ink: #ffffff;
    --ink-soft: #f2f2f2;
    --emboss: #3a3a3a;
  }
  html, body {
    margin: 0;
    padding: 0;
    width: 1200px;
    height: 1059px;
    overflow: hidden;
    background: var(--backdrop);
  }
  .canvas {
    position: relative;
    width: 1200px;
    height: 1059px;
  }
  .card {
    position: absolute;
    background: var(--card);
    box-shadow: 0 12px 28px rgba(0,0,0,0.55);
  }
  .card-front { left: 256px; top: 89px; width: 688px; height: 390px; }
  .card-back  { left: 253px; top: 547px; width: 694px; height: 393px; }

  .name-block {
    position: absolute;
    left: 0;
    top: 72px;
  }
  .name-bar {
    position: absolute;
    left: 0;
    top: 0;
    width: 15px;
    height: 38px;
    background: var(--ink);
  }
  .person-name {
    position: absolute;
    left: 27px;
    top: -5px;
    margin: 0;
    font-family: "Tinos", "Times New Roman", serif;
    font-weight: 700;
    font-size: 23px;
    letter-spacing: 0.3px;
    color: var(--ink);
    white-space: nowrap;
  }
  .person-title {
    position: absolute;
    left: 27px;
    top: 22px;
    margin: 0;
    font-family: "Arimo", Arial, sans-serif;
    font-size: 15px;
    color: var(--ink-soft);
    white-space: nowrap;
  }

  .contact-list {
    position: absolute;
    left: 27px;
    top: 270px;
    margin: 0;
    padding: 0;
    list-style: none;
    font-family: "Arimo", Arial, sans-serif;
    font-size: 16px;
    color: var(--ink-soft);
  }
  .contact-list li {
    display: flex;
    align-items: center;
    height: 25.5px;
    white-space: nowrap;
  }
  .contact-icon {
    width: 13px;
    height: 13px;
    margin-right: 6px;
    fill: var(--ink);
  }

  .company-mark {
    position: absolute;
    right: 40px;
    top: 265px;
    font-family: "Arimo", Arial, sans-serif;
    font-weight: 400;
    color: var(--ink);
    text-align: center;
    text-transform: uppercase;
    letter-spacing: 6px;
    font-size: 15px;
    line-height: 1.5;
  }

  .company-mark-large {
    position: absolute;
    left: 0;
    right: 0;
    top: 168px;
    text-align: center;
    font-family: "Arimo", Arial, sans-serif;
    font-weight: 400;
    font-size: 46px;
    letter-spacing: 10px;
    text-transform: uppercase;
    color: var(--emboss);
  }
</style>
</head>
<body>
<main class="canvas">

  <section class="card card-front" aria-label="Card front">
    <div class="name-block">
      <span class="name-bar"></span>
      <h1 class="person-name">TOBIAS OKAFOR</h1>
      <p class="person-title">Chief Executive Officer</p>
    </div>

    <ul class="contact-list">
      <li>
        <svg class="contact-icon" viewBox="0 0 24 24" aria-hidden="true"><path d="M6.6 10.8c1.4 2.8 3.8 5.1 6.6 6.6l2.2-2.2c.3-.3.7-.4 1-.2 1.1.4 2.3.6 3.6.6.6 0 1 .4 1 1V20c0 .6-.4 1-1 1C10.6 21 3 13.4 3 4c0-.6.4-1 1-1h3.5c.6 0 1 .4 1 1 0 1.3.2 2.5.6 3.6.1.3 0 .7-.2 1z"/></svg>
        780-555-0148
      </li>
      <li>
        <svg class="contact-icon" viewBox="0 0 24 24" aria-hidden="true"><path d="M2 5h20v14H2zM4 7v.5l8 5.5 8-5.5V7l-8 5.2z"/></svg>
        tobiasokafor@marlbeckgroup.example
      </li>
      <li>
        <svg class="contact-icon" viewBox="0 0 24 24" aria-hidden="true"><path d="M12 2a10 10 0 1 0 0 20 10 10 0 0 0 0-20zm-1 17.9A8 8 0 0 1 4.1 11H7c.1 2.6.8 5.2 2 7.4zM4.1 9A8 8 0 0 1 11 4.1V9zm8.9-4.9A8 8 0 0 1 19.9 9H13zm0 15.8V11h6.9a8 8 0 0 1-6.9 8.9z"/></svg>
        www.marlbeckgroup.example
      </li>
    </ul>

    <div class="company-mark">Marlbeck<br>Group of Companies</div>
  </section>

  <section class="card card-back" aria-label="Card back">
    <div class="company-mark-large">Marlbeck</div>
  </section>

</main>
</body>
</html>
```